UK based Drone services needs a pdf / flyer designed.

I am looking to get a flyer advertising what we do. I have added a word document with a little background and what services we offer, please could you add images for each service if possible? We are BRF approved and would like that to be mentioned on the bottom right corner please (logo attached). All our work is carried out with KWO drones, so would ideally like maybe a KWO Pelion 280 rtk image in there. TarlowUAV is the name of the company. Please get back to me if you have any questions.

```html
<!DOCTYPE html>
<html lang="en">
<head>
<meta charset="utf-8">
<title>TarlowUAV Flyer</title>
<link rel="stylesheet" href="https://fonts.googleapis.com/css2?family=Bebas+Neue&family=Montserrat:wght@500;600;700;800&family=Oswald:wght@500&display=swap">
<style>
  :root {
    --backdrop: #b9b9b9;
    --dark: #3d3d3d;
    --dark-top: #4a4a4a;
    --mid-grey: #a8a8a8;
    --light-grey: #bdbdbd;
    --white: #ffffff;
    --ink: #2b2b2b;
    --label-bar: #4a4a4a;
    --badge-blue: #1f6fc0;
    --badge-cyan: #1aa6e0;
  }
  * { box-sizing: border-box; margin: 0; padding: 0; }
  html, body { width: 1200px; height: 2400px; overflow: hidden; }
  body { background: var(--backdrop); font-family: "Montserrat", sans-serif; position: relative; }

  .page {
    position: absolute; left: 206px; width: 785px; height: 1050px;
    background: var(--white); overflow: hidden;
    box-shadow: 4px 5px 8px rgba(0,0,0,0.35);
  }
  .page--front { top: 101px; background: linear-gradient(180deg, var(--dark-top) 400px, #3a3a3a 1050px); }
  .page--back { top: 1265px; }

  .shape-layer { position: absolute; left: 0; top: 0; width: 785px; }

  /* Front */
  .brand {
    position: absolute; left: 40px; top: 134px;
    font-weight: 700; font-size: 46px; letter-spacing: -0.5px; color: #3a3a3a;
  }
  .section-tab {
    position: absolute; left: 34px; top: 437px;
    font-family: "Montserrat", sans-serif; font-weight: 800; font-size: 26px;
    letter-spacing: 0.5px; color: var(--white);
  }
  .about-copy {
    position: absolute; left: 24px; top: 503px; width: 727px;
    color: var(--white); font-size: 20.3px; font-weight: 500; line-height: 29px;
    text-align: justify;
  }
  .about-copy strong { font-weight: 700; }
  .approval {
    position: absolute; left: 442px; top: 915px;
    font-family: "Bebas Neue", sans-serif; font-size: 27px; color: var(--white); letter-spacing: 0.5px;
  }
  .approval-badge {
    position: absolute; left: 658px; top: 905px; width: 94px; height: 125px;
    background: linear-gradient(160deg, var(--badge-cyan), var(--badge-blue));
    border: 2px solid var(--white);
  }
  .contact-label {
    position: absolute; left: 32px; top: 982px;
    font-family: "Bebas Neue", sans-serif; font-size: 40px; color: var(--white); letter-spacing: 1px;
  }
  .contact-lines { position: absolute; left: 325px; top: 975px; color: var(--ink); }
  .contact-phone { display: flex; align-items: center; gap: 6px; font-weight: 600; font-size: 28px; line-height: 34px; }
  .contact-web { font-weight: 500; font-size: 25px; line-height: 30px; letter-spacing: 0.5px; margin-left: 2px; }

  /* Back */
  .intro-copy {
    position: absolute; left: 38px; top: 52px; width: 710px;
    color: var(--white); font-size: 19.5px; font-weight: 500; line-height: 27.5px;
  }
  .intro-copy p + p { margin-top: 27px; }
  .services-title {
    position: absolute; left: 22px; top: 440px;
    font-weight: 800; font-size: 34px; color: #3c3c3c; letter-spacing: 0.5px;
  }
  .services-rule { position: absolute; left: 22px; top: 480px; width: 108px; height: 3px; background: #8a8a8a; }

  .label-bar {
    position: absolute; left: 0; width: 785px; height: 46px; background: var(--label-bar);
    display: grid; grid-template-columns: 253px 257px 275px;
  }
  .label-bar--top { top: 518px; }
  .label-bar--bottom { top: 975px; }
  .service-label {
    display: flex; align-items: center; justify-content: center; text-align: center;
    font-family: "Oswald", sans-serif; font-weight: 500; font-size: 24px; line-height: 21px;
    color: var(--white); text-transform: uppercase; letter-spacing: -0.3px;
    border-right: 3px solid var(--white);
  }
  .service-label:last-child { border-right: none; }
  .service-label--small { font-size: 20px; line-height: 21px; }
  .service-label--large { font-size: 30px; }

  .service-photo {
    position: absolute; width: 226px; height: 180px;
    border-bottom: 8px solid #a5a5a5;
  }
  .col-1 { left: 16px; } .col-2 { left: 272px; } .col-3 { left: 527px; }
  .row-1 { top: 576px; } .row-2 { top: 793px; }
  .photo-commercial { background: linear-gradient(100deg, #c9d4dc 0%, #7fa0c4 35%, #4f86c4 100%); }
  .photo-mapping { background: linear-gradient(180deg, #6f8a58 0%, #4f6e3a 60%, #2f4a28 100%); }
  .photo-aerial { background: linear-gradient(180deg, #6e95cf 0%, #a8bfdd 70%, #8c9298 100%); }
  .photo-solar { background: linear-gradient(170deg, #6f9bd6 0%, #b8cde6 65%, #34528a 100%); }
  .photo-estate { background: linear-gradient(180deg, #9fb7d3 0%, #6c7f6a 45%, #3a3f3a 75%, #6d7c3e 100%); }
  .photo-agri { background: linear-gradient(180deg, #2f6fc4 0%, #5e94d6 45%, #4f8a3a 70%, #2d5a24 100%); }
</style>
</head>
<body>

<section class="page page--front">
  <svg class="shape-layer" height="400" viewBox="0 0 785 400" aria-hidden="true">
    <defs>
      <linearGradient id="heroSky" x1="0" y1="0" x2="1" y2="0">
        <stop offset="0" stop-color="#f4f6f9"/>
        <stop offset="0.45" stop-color="#c6d3e6"/>
        <stop offset="1" stop-color="#7d9cc9"/>
      </linearGradient>
    </defs>
    <polygon points="0,0 785,0 785,376 409,390 335,309 0,309" fill="url(#heroSky)"/>
    <polygon points="0,309 335,309 409,390 785,376 785,382 400,394 320,338 0,338" fill="var(--light-grey)"/>
  </svg>
  <div role="img" aria-label="Photo of a KWO Pelion 280 rtk drone flying against a blue sky" style="position:absolute;left:370px;top:60px;width:400px;height:300px;"></div>

  <div class="brand">TarlowUAV</div>

  <svg class="shape-layer" style="top:430px" height="40" viewBox="0 0 785 40" aria-hidden="true">
    <polygon points="0,6 300,6 335,36 0,36" fill="var(--mid-grey)"/>
    <line x1="335" y1="36" x2="734" y2="36" stroke="var(--mid-grey)" stroke-width="2"/>
  </svg>
  <h2 class="section-tab">ABOUT US</h2>

  <p class="about-copy"><strong>Unmanned Arial Vehicles (UAV's)</strong> are revolutionizing the way industries are able to work. With current advances in technology, drones are opening doors that weren't available before. With the ability to reach difficult and dangerous areas, they remove the human element and change the scope of what's safely possible. Capturing live Ultra High-Definition footage of<br>unreachable areas and making working at heights a thing of the past.<br>Drones are safer, faster, more cost-effective and a highly accurate<br>alternative. Not only do you have the chance to inspect<br>dangerous areas live, but you also get photographs and/or 4K Ultra HD video footage to review at a later date. No need to send someone back out to the area to double-check damage, you have it all on record.</p>

  <div class="approval">WE ARE BRF APPROVED</div>

  <svg class="shape-layer" style="top:965px" height="85" viewBox="0 0 785 85" aria-hidden="true">
    <rect x="0" y="0" width="785" height="85" fill="var(--white)"/>
    <polygon points="0,0 224,0 264,85 0,85" fill="var(--mid-grey)"/>
    <polygon points="224,0 240,0 280,85 264,85" fill="#1e1e1e"/>
  </svg>
  <div class="approval-badge" aria-label="BRF approval badge"></div>
  <div class="contact-label">CONTACT US</div>
  <div class="contact-lines">
    <div class="contact-phone">
      <svg width="30" height="30" viewBox="0 0 30 30" aria-hidden="true">
        <circle cx="15" cy="15" r="15" fill="var(--ink)"/>
        <path d="M10 8c1-1 2-1 2.6 0l1.4 2.4c.4.7.2 1.4-.4 1.9l-.9.7c.8 1.8 2.2 3.3 4 4.1l.8-.9c.5-.6 1.2-.7 1.9-.3l2.4 1.4c.9.6.9 1.6 0 2.6-1.4 1.5-3.4 1.7-6 .3-3-1.7-5.2-4-6.5-6.9-1-2.4-.8-4.1.7-5.3z" fill="var(--white)"/>
      </svg>
      <span>(000) 000 0000</span>
    </div>
    <div class="contact-web">www.company.com</div>
  </div>
</section>

<section class="page page--back">
  <svg class="shape-layer" height="480" viewBox="0 0 785 480" aria-hidden="true">
    <defs>
      <linearGradient id="backDark" x1="0" y1="0" x2="0" y2="1">
        <stop offset="0" stop-color="#4b4b4b"/>
        <stop offset="1" stop-color="#3e3e3e"/>
      </linearGradient>
    </defs>
    <rect x="0" y="0" width="785" height="480" fill="url(#backDark)"/>
    <polygon points="0,400 335,400 414,468 785,454 785,480 0,480" fill="var(--mid-grey)"/>
    <polygon points="0,417 353,417 418,476 785,470 785,480 0,480" fill="var(--white)"/>
  </svg>

  <div class="intro-copy">
    <p>TarlowUAV is fully equipped with the latest and most suitable drones for your business or personal needs. From a small roof survey to a full wind turbine site inspection. No project is too small or too large, take advantage of using UAV's now!</p>
    <p>Here at TarlowUAV, we pride ourselves on being affordable and offering a great product to our clients. We have a comprehensive list of services that we offer to any business or individual across the UK. Our UAV pilots are GVC licensed and have gained<br>Operational Authorization from the British Remote Flight Board<br>allowing us to carry out commercial work in the UK.</p>
  </div>

  <h2 class="services-title">SERVICES</h2>
  <div class="services-rule"></div>

  <div class="label-bar label-bar--top">
    <div class="service-label">Commercial Inspections</div>
    <div class="service-label">Mapping / Surveys</div>
    <div class="service-label service-label--small">Aerial Photography /<br>Videography</div>
  </div>

  <div class="service-photo col-1 row-1 photo-commercial" role="img" aria-label="Drone inspecting a glass office building"></div>
  <div class="service-photo col-2 row-1 photo-mapping" role="img" aria-label="Drone hovering over a green hillside for mapping"></div>
  <div class="service-photo col-3 row-1 photo-aerial" role="img" aria-label="Drone flying above an electrical substation"></div>
  <div class="service-photo col-1 row-2 photo-solar" role="img" aria-label="Drone flying over solar panels"></div>
  <div class="service-photo col-2 row-2 photo-estate" role="img" aria-label="Drone hovering above a large house"></div>
  <div class="service-photo col-3 row-2 photo-agri" role="img" aria-label="Drone flying over rows of crops"></div>

  <div class="label-bar label-bar--bottom">
    <div class="service-label">Solar Panel Inspections</div>
    <div class="service-label">Real Estate / Planning</div>
    <div class="service-label service-label--large">Agriculture</div>
  </div>
</section>

</body>
</html>
```